Design a website for a newly developed Delta 8 THC Company

Design a responsive Website with the following goals in mind:
- Built on Wordpress/WooCommerce theme. Please use this when designing for ease of integration.
- Build trust with website visitors with an engaging, informative content driven website, that leads to a conversion of product purchase and repeat business. We will also be driving consumers to businesses that carry our products as well.
- The website will embody a lifestyle feel and make the visitor identify with the content.
- The website will allow for super charged SEO and other digital marketing and advertising strategies and tactics used to increase discovery, awareness, and conversion.
Please see additional goals in the uploaded files.
Target Market(s)
Male/Female 21-
Industry/Entity Type
Cannabis/Hemp
Coding
Coded - Design and coding required
Number of Pages Required
5+ page
Font styles to use
Other font styles liked:
- Montserrat
Look and feel
Each slider illustrates characteristics of the customer's brand and the style your logo design should communicate.

```html
<!DOCTYPE html>
<html lang="en">
<head>
<meta charset="utf-8">
<title>Lumora — Delta-8 Hemp Goods</title>
<link href="https://fonts.googleapis.com/css2?family=Montserrat:wght@400;500;600;700;800&display=swap" rel="stylesheet">
<style>
:root{
  --gold:#f5a50a;
  --gold-dark:#d98c00;
  --ink:#1d1d1d;
  --night:#151515;
  --text:#555;
  --muted:#8a8a8a;
  --line:#e4e4e4;
  --white:#fff;
  --pouch:#161616;
  --leaf:#3f7a2c;
}
*{box-sizing:border-box;margin:0;padding:0}
html,body{width:1200px;height:3472px;overflow:hidden}
body{font-family:'Montserrat',sans-serif;color:var(--ink);background:var(--white);position:relative}
a{color:inherit;text-decoration:none}
.btn{display:inline-block;background:var(--gold);color:var(--white);font-weight:700;font-size:12px;letter-spacing:.5px;padding:11px 22px;border-radius:3px;text-transform:uppercase}
.accent{color:var(--gold)}

/* header */
.site-header{position:relative;height:184px;background:var(--white)}
.brand{position:absolute;left:70px;top:52px;display:flex;align-items:center;gap:10px}
.brand-dot{width:20px;height:20px;border-radius:50%;background:var(--gold)}
.brand-name{font-weight:700;font-size:22px;letter-spacing:3px;color:var(--gold)}
.topbar{position:absolute;left:272px;right:0;top:0;height:36px;background:var(--night);color:var(--white);display:flex;align-items:center;font-size:11px;padding:0 40px 0 14px}
.store-tag{background:var(--gold);font-weight:700;padding:4px 10px;border-radius:2px}
.topbar .user{margin-left:auto;display:flex;gap:36px;align-items:center}
.topbar .user span{display:flex;align-items:center;gap:6px}
.toolbar{position:absolute;left:272px;right:40px;top:36px;height:104px;display:flex;align-items:center;font-size:11px;color:var(--text);padding-left:14px}
.search{margin-left:82px;display:flex;align-items:center;border:1px solid var(--line);height:32px;width:420px}
.search .field{flex:1}
.search .cat{background:var(--gold);color:var(--white);font-weight:700;height:100%;display:flex;align-items:center;padding:0 14px;gap:6px}
.search .go{width:34px;height:100%;display:flex;align-items:center;justify-content:center}
.cart{margin-left:auto;display:flex;gap:18px;align-items:center}
.main-nav{position:absolute;left:0;right:0;top:144px;height:40px;background:var(--gold);display:flex;justify-content:center;gap:34px;align-items:center;font-size:12px;font-weight:600;color:var(--ink)}

/* hero */
.hero{position:relative;height:496px;overflow:hidden}
.hero-photo{position:absolute;inset:0;background:
  radial-gradient(ellipse 300px 260px at 72% 58%,rgba(10,10,10,.95),rgba(10,10,10,0) 70%),
  radial-gradient(ellipse 220px 220px at 90% 62%,rgba(12,12,12,.9),rgba(12,12,12,0) 70%),
  radial-gradient(ellipse 260px 160px at 95% 15%,#2f4a2a,rgba(47,74,42,0) 75%),
  linear-gradient(180deg,#8fb4c4 0%,#bcd3d8 30%,#6f8f96 48%,#3d5a5e 62%,#1f2d2c 80%,#111713 100%)}
.hero-copy{position:absolute;left:112px;top:138px;color:var(--white)}
.hero-copy h1{font-size:44px;font-weight:500;line-height:1.15;letter-spacing:1px;margin-bottom:26px;text-shadow:0 1px 6px rgba(0,0,0,.25)}
.dots{position:absolute;left:116px;bottom:22px;display:flex;gap:6px}
.dots i{width:6px;height:6px;border-radius:50%;background:#bbb}
.dots i:first-child{background:var(--white)}

/* about */
.about{height:520px;position:relative}
.about-photo{position:absolute;left:144px;top:88px;width:416px;height:276px;background:
  radial-gradient(ellipse 110px 130px at 58% 44%,var(--pouch),rgba(22,22,22,0) 85%),
  radial-gradient(ellipse 90px 50px at 38% 72%,var(--leaf),rgba(63,122,44,0) 80%),
  linear-gradient(135deg,#8c8c8c,#5e5e5e)}
.about-copy{position:absolute;left:622px;top:86px;width:440px}
.about-copy h2{font-size:30px;font-weight:700;margin-bottom:18px}
.about-copy p{font-size:12px;line-height:1.75;color:var(--text);margin-bottom:20px}

/* featured */
.featured{position:relative;height:660px;overflow:hidden}
.featured-photo{position:absolute;inset:0;background:
  radial-gradient(ellipse 360px 260px at 12% 85%,rgba(52,70,40,.8),rgba(52,70,40,0) 70%),
  radial-gradient(ellipse 340px 240px at 90% 20%,rgba(48,64,38,.7),rgba(48,64,38,0) 70%),
  linear-gradient(180deg,#3c3e3a 0%,#5a5c56 50%,#474843 100%)}
.featured h2,.services h2{text-align:center;font-size:28px;font-weight:700;position:relative}
.featured h2{color:var(--white);padding-top:82px}
.product-row{position:absolute;left:112px;top:140px;display:flex;gap:26px}
.product{width:224px;height:292px;background:var(--white);position:relative;text-align:center}
.product-shot{height:188px;margin:10px 10px 0;background:
  radial-gradient(ellipse 62px 80px at 50% 52%,var(--pouch) 55%,rgba(22,22,22,0) 100%),
  linear-gradient(160deg,#f4f4f4,#dcdcdc)}
.product h3{font-size:14px;font-weight:600;margin-top:14px}
.price{font-size:11px;color:var(--muted);margin-top:6px}
.stars{color:var(--gold);font-size:13px;letter-spacing:2px;margin-top:6px}
.badge{position:absolute;left:10px;top:10px;background:var(--gold);color:var(--white);font-size:9px;font-weight:700;padding:3px 8px}
.options{position:absolute;left:10px;right:10px;top:176px;background:var(--gold);color:var(--white);font-size:10px;font-weight:700;padding:5px 0}
.arrow{position:absolute;top:280px;width:22px;height:22px;border-radius:50%;background:var(--white);display:flex;align-items:center;justify-content:center}
.featured .cta{position:absolute;left:0;right:0;top:520px;text-align:center}

/* services */
.services{height:680px;position:relative}
.services h2{padding-top:92px}
.rule{width:46px;height:3px;background:var(--gold);margin:10px auto 0}
.service-grid{position:absolute;left:112px;top:170px;display:grid;grid-template-columns:repeat(3,308px);gap:30px 26px}
.service{height:128px;border:1px solid var(--line);box-shadow:0 2px 8px rgba(0,0,0,.06);display:flex;gap:16px;padding:22px 18px}
.service .icon{flex:0 0 52px;height:52px;border-radius:50%;border:2px solid var(--gold);display:flex;align-items:center;justify-content:center}
.service h3{font-size:13px;font-weight:700;text-transform:uppercase;margin:4px 0 8px}
.service p{font-size:11px;color:var(--text);line-height:1.55}
.service a{display:block;margin-top:6px;font-size:11px;color:var(--gold);font-weight:600}

/* promo */
.promo{position:relative;height:308px;overflow:hidden}
.promo-photo{position:absolute;inset:0;background:
  radial-gradient(ellipse 130px 150px at 78% 42%,#0c0c0c 50%,rgba(12,12,12,0) 100%),
  radial-gradient(ellipse 200px 70px at 42% 88%,rgba(63,122,44,.75),rgba(63,122,44,0) 80%),
  linear-gradient(180deg,rgba(0,0,0,0) 65%,#5a4230 66%,#3b2a1e 100%),
  linear-gradient(100deg,#0e0e0e 0%,#1c1a18 55%,#2e2a26 100%)}
.promo-copy{position:absolute;left:112px;top:82px;color:var(--white)}
.promo-copy small{font-size:13px;letter-spacing:1px;display:block;margin-bottom:10px}
.promo-copy h2{font-size:36px;font-weight:500;line-height:1.2;margin-bottom:22px}

/* newsletter */
.newsletter{height:252px;position:relative}
.newsletter-copy{position:absolute;left:112px;top:72px;width:460px}
.newsletter-copy h2{font-size:24px;font-weight:700;margin-bottom:14px}
.newsletter-copy p{font-size:12px;color:var(--text);line-height:1.6}
.subscribe{position:absolute;left:680px;top:74px;width:408px}
.subscribe .field{height:38px;border:1px solid var(--line);font-size:11px;color:var(--muted);display:flex;align-items:center;padding:0 14px;margin-bottom:12px}
.subscribe .btn{padding:10px 26px}

/* footer */
.site-footer{position:relative;height:332px;background:var(--night);color:#cfcfcf}
.footer-brand{position:absolute;left:112px;top:60px;display:flex;align-items:center;gap:10px}
.social{position:absolute;left:112px;top:190px;display:flex;gap:12px}
.social i{width:34px;height:34px;border-radius:50%;border:1px solid #666;display:block}
.footer-col{position:absolute;top:60px}
.footer-col h4{color:var(--white);font-size:15px;font-weight:600;margin-bottom:8px}
.footer-col h4::after{content:"";display:block;width:34px;height:2px;background:var(--gold);margin-top:6px}
.footer-col li{list-style:none;font-size:11px;line-height:1.85}
.legal{position:absolute;left:0;right:0;bottom:0;height:40px;background:#0b0b0b;font-size:10px;color:#9a9a9a;display:flex;align-items:center;padding:0 112px}
.legal nav{margin-left:auto;display:flex;gap:40px;margin-right:60px}
.chat{position:absolute;right:30px;top:3px;width:34px;height:34px;border-radius:50%;background:var(--gold)}
</style>
</head>
<body>

<header class="site-header">
  <a class="brand" href="#"><span class="brand-dot"></span><span class="brand-name">LUMORA</span></a>
  <div class="topbar">
    <span class="store-tag">STORE: 40718</span>
    <div class="user">
      <span><svg width="12" height="12" viewBox="0 0 12 12"><circle cx="6" cy="4" r="2.5" fill="none" stroke="#fff"/><path d="M1.5 11c.5-3 8.5-3 9 0" fill="none" stroke="#fff"/></svg>Hi, Marcus Delane</span>
      <span>Create Account</span>
      <span>Sign In</span>
    </div>
  </div>
  <div class="toolbar">
    <span>48 Harbor Lane Milltown, MT 20418</span>
    <div class="search">
      <span class="field"></span>
      <span class="cat">PRODUCT <svg width="8" height="5" viewBox="0 0 8 5"><path d="M0 0l4 5 4-5z" fill="#fff"/></svg></span>
      <span class="go"><svg width="14" height="14" viewBox="0 0 14 14"><circle cx="6" cy="6" r="4.5" fill="none" stroke="#555" stroke-width="1.5"/><path d="M9.5 9.5L13 13" stroke="#555" stroke-width="1.5"/></svg></span>
    </div>
    <div class="cart">
      <svg width="18" height="16" viewBox="0 0 18 16"><path d="M9 15S1 10 1 5a4 4 0 0 1 8-1 4 4 0 0 1 8 1c0 5-8 10-8 10z" fill="none" stroke="#333" stroke-width="1.4"/></svg>
      <svg width="20" height="18" viewBox="0 0 20 18"><path d="M1 1h3l2 10h11l2-7H5" fill="none" stroke="#333" stroke-width="1.4"/><circle cx="8" cy="15" r="1.5" fill="#333"/><circle cx="16" cy="15" r="1.5" fill="#333"/></svg>
    </div>
  </div>
  <nav class="main-nav">
    <a>HOME</a><a>SPECIAL</a><a>BLOG</a><a>MANAGE PRODUCT</a><a>ABOUT US</a><a>OFFERS</a><a>CONTACT US</a>
  </nav>
</header>

<section class="hero">
  <div class="hero-photo" role="img" aria-label="Misty mountain lake under a pale sky with three black gummy pouches standing on a dark ledge"></div>
  <div class="hero-copy">
    <h1>SALE UP TO 50%<br>OFF EVERYTHING</h1>
    <a class="btn" href="#">Shop Now</a>
  </div>
  <div class="dots"><i></i><i></i><i></i><i></i></div>
</section>

<section class="about">
  <div class="about-photo" role="img" aria-label="Black gummy pouch lying beside a green hemp leaf on a grey surface"></div>
  <div class="about-copy">
    <h2>ABOUT <span class="accent">US</span></h2>
    <p>Our hemp-derived Delta-8 products are crafted in small batches, lab tested for purity and made for adults who value calm, balance and quality. We partner with trusted growers and share every certificate so you always know exactly what is inside each pack before you buy it from us.</p>
    <a class="btn" href="#">Learn More</a>
  </div>
</section>

<section class="featured">
  <div class="featured-photo" role="img" aria-label="Dark hemp foliage backdrop"></div>
  <h2>FEATURED <span class="accent">PRODUCTS</span></h2>
  <span class="arrow" style="left:96px"><svg width="8" height="10" viewBox="0 0 8 10"><path d="M6 1L2 5l4 4" fill="none" stroke="#333" stroke-width="1.5"/></svg></span>
  <span class="arrow" style="right:96px"><svg width="8" height="10" viewBox="0 0 8 10"><path d="M2 1l4 4-4 4" fill="none" stroke="#333" stroke-width="1.5"/></svg></span>
  <div class="product-row">
    <article class="product">
      <div class="product-shot" role="img" aria-label="Black gummy pouch"></div>
      <span class="badge">SALE</span>
      <h3>Minim Deniquis Eostrud</h3>
      <p class="price">$110.00 – $120.00</p>
      <p class="stars">★★★★★</p>
    </article>
    <article class="product">
      <div class="product-shot" role="img" aria-label="Black gummy pouch"></div>
      <span class="options">CHOOSE OPTIONS</span>
      <h3>Minim Deniquis Eostrud</h3>
      <p class="price">$110.00 – $120.00</p>
      <p class="stars">★★★★★</p>
    </article>
    <article class="product">
      <div class="product-shot" role="img" aria-label="Black gummy pouch"></div>
      <h3>Minim Deniquis Eostrud</h3>
      <p class="price">$110.00 – $120.00</p>
      <p class="stars">★★★★★</p>
    </article>
    <article class="product">
      <div class="product-shot" role="img" aria-label="Black gummy pouch"></div>
      <h3>Minim Deniquis Eostrud</h3>
      <p class="price">$110.00 – $120.00</p>
      <p class="stars">★★★★★</p>
    </article>
  </div>
  <div class="cta"><a class="btn" href="#">Shop Now</a></div>
</section>

<section class="services">
  <h2>OUR <span class="accent">SERVICES</span></h2>
  <div class="rule"></div>
  <div class="service-grid">
    <div class="service"><span class="icon"><svg width="24" height="24" viewBox="0 0 24 24"><path d="M3 20h18M6 17V11M11 17V7M16 17V9" stroke="#f5a50a" stroke-width="2" fill="none"/></svg></span><div><h3>Financial Management</h3><p>Clear pricing tools that help partner stores plan each month.</p><a>Read more</a></div></div>
    <div class="service"><span class="icon"><svg width="24" height="24" viewBox="0 0 24 24"><rect x="4" y="6" width="16" height="13" fill="none" stroke="#f5a50a" stroke-width="2"/><path d="M4 10h16" stroke="#f5a50a" stroke-width="2"/></svg></span><div><h3>Inventory Management</h3><p>Simple stock tracking so shelves stay full and fresh.</p><a>Read more</a></div></div>
    <div class="service"><span class="icon"><svg width="24" height="24" viewBox="0 0 24 24"><path d="M12 3l8 3v6c0 5-4 8-8 9-4-1-8-4-8-9V6z" fill="none" stroke="#f5a50a" stroke-width="2"/></svg></span><div><h3>Loss Prevention</h3><p>Secure packaging and handling guidance for every retail site.</p><a>Read more</a></div></div>
    <div class="service"><span class="icon"><svg width="24" height="24" viewBox="0 0 24 24"><path d="M4 10v4h4l8 5V5L8 10z" fill="none" stroke="#f5a50a" stroke-width="2"/></svg></span><div><h3>Marketing &amp; Promo...</h3><p>Ready-made displays and campaigns that bring shoppers in.</p><a>Read more</a></div></div>
    <div class="service"><span class="icon"><svg width="24" height="24" viewBox="0 0 24 24"><circle cx="9" cy="8" r="3" fill="none" stroke="#f5a50a" stroke-width="2"/><circle cx="17" cy="9" r="2.5" fill="none" stroke="#f5a50a" stroke-width="2"/><path d="M3 20c0-4 12-4 12 0M15 15c3-1 6 1 6 4" fill="none" stroke="#f5a50a" stroke-width="2"/></svg></span><div><h3>People Management</h3><p>Staff training on products, dosing and responsible sales.</p><a>Read more</a></div></div>
    <div class="service"><span class="icon"><svg width="24" height="24" viewBox="0 0 24 24"><path d="M3 10l2-5h14l2 5M5 10v10h14V10M3 10h18" fill="none" stroke="#f5a50a" stroke-width="2"/></svg></span><div><h3>Store Environment</h3><p>Layout ideas that make every visit feel calm and welcoming.</p><a>Read more</a></div></div>
    <div class="service"><span class="icon"><svg width="24" height="24" viewBox="0 0 24 24"><rect x="3" y="4" width="18" height="12" fill="none" stroke="#f5a50a" stroke-width="2"/><path d="M9 20h6M12 16v4" stroke="#f5a50a" stroke-width="2"/></svg></span><div><h3>Store Systems</h3><p>Point of sale setup and reporting made quick and easy.</p><a>Read more</a></div></div>
    <div class="service"><span class="icon"><svg width="24" height="24" viewBox="0 0 24 24"><path d="M3 9h14l-3-3M21 15H7l3 3" fill="none" stroke="#f5a50a" stroke-width="2"/></svg></span><div><h3>Business to Business</h3><p>Wholesale ordering with fast delivery to your shop door.</p><a>Read more</a></div></div>
    <div class="service"><span class="icon"><svg width="24" height="24" viewBox="0 0 24 24"><path d="M4 18l5-6 4 3 7-9" fill="none" stroke="#f5a50a" stroke-width="2"/></svg></span><div><h3>New and Trendin...</h3><p>Early access to seasonal flavors and limited releases.</p><a>Read more</a></div></div>
  </div>
</section>

<section class="promo">
  <div class="promo-photo" role="img" aria-label="Black gummy pouch on a dark wooden table beside a green hemp leaf"></div>
  <div class="promo-copy">
    <small>SUMMER 2021 OFFERS</small>
    <h2>UPTO 50% OFF ON ALL<br>PRODUCTS</h2>
    <a class="btn" href="#">Shop Now</a>
  </div>
</section>

<section class="newsletter">
  <div class="newsletter-copy">
    <h2>SUBSCRIBE TO <span class="accent">OUR NEWSLETTER</span></h2>
    <p>Get new product drops, partner store news and members-only offers in your inbox.</p>
  </div>
  <form class="subscribe">
    <div class="field">YOUR EMAIL ADDRESS</div>
    <span class="btn">Submit</span>
  </form>
</section>

<footer class="site-footer">
  <div class="footer-brand"><span class="brand-dot"></span><span class="brand-name">LUMORA</span></div>
  <div class="social"><i></i><i></i><i></i><i></i></div>
  <div class="footer-col" style="left:470px"><h4>Quick Links</h4><ul><li>Home</li><li>Special</li><li>Blog</li><li>Manage Product</li><li>About Us</li><li>Offers</li><li>Contact Us</li></ul></div>
  <div class="footer-col" style="left:700px"><h4>Links</h4><ul><li>FAQs</li><li>Login</li><li>Privacy</li><li>Accessibility</li><li>Sitemap</li></ul></div>
  <div class="footer-col" style="left:900px"><h4>Customer Support</h4><ul><li>Terms Of Use</li><li>Track Orders</li><li>Shipping</li><li>Cancellation</li><li>Careers</li><li>Site Map</li></ul></div>
  <div class="legal">
    <span>Copyright © 2021 Lumora. All rights reserved.</span>
    <nav><a>Privacy Policy</a><a>Terms and Use</a></nav>
    <span class="chat"></span>
  </div>
</footer>

</body>
</html>
```